Stylist/Barber Standup Sign for Hair Regrowth Company

We want to design an attractive and eye-catching sign for hair stylists and barbers to sit on their workstations to attract the attention of their clients regarding hair loss and encourage them to speak to their stylist about it of they are would like to seek treatment.
50% of men and 25% of women suffer from hair loss but most are in denial that it is happening or too embarrassed to talk about it.

Copy for the flyer is as follows:

[Section 1:]
This flyer has been placed here/designed to spark conversation about hair loss

[Section 2:]
The truth is...
73% of people believe their hair is thinning
They are right

[Section 3:]
If you've got questions, your stylist or barber has answers.

Additional Background Information:

Primary target audience is men between the ages of 25-45, secondary target audience is men 46-60

Current Consumer Perception? (in the first person) “I’ve been thinking about my hair. I think it’s getting thinner and I’m scared, worried and don’t know what to do. But I don’t know if there is anything that really works. I’ve tried other things and nothing‘s worked.”

Tonality of materials? Very guy friendly, matter of fact, authoritative, its what you might hear from your best friend. Confident. Encouraging, but with a sense of urgency.

Please use our brand colors, but do not include our logo or brand name.
Colors are as follows:
Green: #4ca26f
Light Grey: #999999
Dark Grey: #262626

I have attached print templates in both PDF and Jpeg, please use those to provide final ready to print documents if you are selected.

Target Market(s)

Industry/Entity Type

Health And Wellness

Font styles to use
Sans Serif

Colors
00a990
ffffff
333333
cbcbcb

Requirements
Must have
• We want to get across the following messaging. Ideally you will submit a design using our copy and if you think you can do better, please feel free to submit another design with your own copy/messaging. If you can do it better we would love to select you :-)
• Our copy?
• This flyer has been placed here/designed to spark conversation about hair loss
• The truth is...
• 73% of people believe their hair is thinning
• They are right
• If you've got questions, your stylist or barber has answers
• Also please use our brand colors:
• Green: #4ca26f
• Light Grey: #999999
• Dark Grey: #262626
Should not have
• dont add any logos, images or ornate design. this needs to be simple, easy to ready and eye catching.
• do not use the color red in any capacity.

```html
<!DOCTYPE html>
<html lang="en">
<head>
<meta charset="utf-8">
<title>Hair Loss Conversation Standup Sign</title>
<link rel="stylesheet" href="https://fonts.googleapis.com/css2?family=Raleway:ital,wght@0,400;0,700;1,400&display=swap">
<style>
  :root {
    --backdrop: #d6d6d6;
    --sign-light: #f4f3f5;
    --sign-mid: #e4e2e6;
    --frame: #333333;
    --green: #00a990;
    --band-green: #15ab8f;
    --heading-grey: #4a4a4a;
    --body-black: #111111;
    --note-grey: #444444;
    --white: #ffffff;
  }
  * { box-sizing: border-box; margin: 0; padding: 0; }
  html, body {
    width: 943px;
    height: 1200px;
    overflow: hidden;
    background: var(--backdrop);
    font-family: "Raleway", sans-serif;
  }
  .sign {
    position: absolute;
    left: 86px;
    top: 28px;
    width: 771px;
    height: 1144px;
    overflow: hidden;
    box-shadow: 0 6px 18px rgba(0,0,0,0.25);
  }
  .sign-backdrop {
    position: absolute;
    inset: 0;
    background: linear-gradient(100deg, var(--sign-mid) 0%, var(--sign-light) 45%, var(--sign-light) 100%);
  }
  .sign-frame {
    position: absolute;
    left: 17px;
    top: 17px;
    right: 17px;
    bottom: 17px;
    border: 1.5px solid var(--frame);
  }
  .intro {
    position: absolute;
    right: 42px;
    top: 47px;
    width: 420px;
    text-align: right;
    color: var(--green);
    font-size: 40px;
    line-height: 50px;
    font-weight: 400;
  }
  .truth-heading {
    position: absolute;
    right: 42px;
    top: 524px;
    color: var(--heading-grey);
    font-size: 57px;
    line-height: 60px;
    font-weight: 700;
  }
  .statistic {
    position: absolute;
    right: 52px;
    top: 652px;
    text-align: right;
    color: var(--body-black);
    font-size: 35px;
    line-height: 49px;
    font-weight: 400;
  }
  .verdict {
    position: absolute;
    right: 42px;
    top: 800px;
    color: var(--note-grey);
    font-size: 35px;
    line-height: 44px;
    font-style: italic;
  }
  .answer-band {
    position: absolute;
    left: 0;
    right: 0;
    top: 966px;
    height: 106px;
    background: var(--band-green);
    display: flex;
    align-items: center;
    justify-content: center;
    text-align: center;
    color: var(--white);
    font-size: 27px;
    line-height: 37px;
  }
</style>
</head>
<body>
  <main class="sign">
    <div class="sign-backdrop" role="img" aria-label="Photo of barber tools on white wooden boards: clippers, comb, straight razor, thinning scissors, bowl and brush"></div>
    <div class="sign-frame"></div>

    <p class="intro">This flyer has been placed here/designed to spark conversation about hair loss</p>

    <h1 class="truth-heading">The truth is...</h1>

    <p class="statistic">73% of people believe their<br>hair is thinning</p>

    <p class="verdict">They are right!</p>

    <div class="answer-band">
      <p>If you've got questions,<br>your stylist or barber has answers</p>
    </div>
  </main>
</body>
</html>
```